Modern Business Card

Modern professional business card with more than just logo and demographic info. Something memorable.

We are a trendy/modern chiropractic group with an emphasis on neurology, hence the minimalist-type brain logo. We want to convey that modern and technical aspect with professionalism and the elite nature of our practice environment.

```html
<!DOCTYPE html>
<html lang="en">
<head>
<meta charset="utf-8">
<title>Meridian Chiropractic – Business Card</title>
<link rel="stylesheet" href="https://fonts.googleapis.com/css2?family=Caladea:ital,wght@0,400;0,700;1,400&display=swap">
<style>
  :root {
    --card-bg: #ffffff;
    --ink: #111111;
    --body-ink: #222222;
    --accent-blue: #4a7fc4;
    --frame: #000000;
  }
  html, body {
    margin: 0;
    padding: 0;
    overflow: hidden;
    background: var(--card-bg);
  }
  .card {
    position: relative;
    width: 1200px;
    height: 720px;
    box-sizing: border-box;
    border: 2px solid var(--frame);
    background: var(--card-bg);
    font-family: "Caladea", "Cambria", Georgia, serif;
    overflow: hidden;
  }
  .trim-guides {
    position: absolute;
    inset: 0;
  }
  .brand {
    position: absolute;
    left: 94px;
    top: 94px;
    display: flex;
    align-items: center;
    gap: 20px;
  }
  .brand-mark {
    width: 168px;
    height: 168px;
    background: var(--accent-blue);
    flex: none;
  }
  .brand-name {
    margin: 0;
    color: var(--ink);
    font-weight: 400;
    line-height: 1;
  }
  .brand-name .line-primary {
    display: block;
    font-size: 112px;
    letter-spacing: 1px;
  }
  .brand-name .line-secondary {
    display: block;
    font-size: 60px;
    letter-spacing: 1px;
    margin-top: 4px;
  }
  .contact {
    position: absolute;
    left: 94px;
    top: 390px;
    color: var(--body-ink);
  }
  .contact-name {
    margin: 0;
    color: var(--accent-blue);
    font-weight: 700;
    font-size: 46px;
    line-height: 1.1;
  }
  .contact-title {
    margin: 4px 0 0;
    font-style: italic;
    font-size: 34px;
    line-height: 1.2;
  }
  .contact-details {
    margin: 2px 0 0;
    font-size: 35px;
    line-height: 42px;
  }
</style>
</head>
<body>
  <div class="card">
    <svg class="trim-guides" width="1196" height="716" viewBox="0 0 1196 716" aria-hidden="true">
      <g fill="none" stroke="var(--frame)" stroke-width="2.5">
        <path d="M39 64 V39 H64"/>
        <path d="M1132 39 H1157 V64"/>
        <path d="M39 652 V677 H64"/>
        <path d="M1132 677 H1157 V652"/>
        <line x1="124" y1="39" x2="1100" y2="39" stroke-dasharray="38 73"/>
        <line x1="124" y1="677" x2="1100" y2="677" stroke-dasharray="38 73"/>
        <line x1="39" y1="116" x2="39" y2="620" stroke-dasharray="38 73"/>
        <line x1="1157" y1="116" x2="1157" y2="620" stroke-dasharray="38 73"/>
      </g>
    </svg>

    <header class="brand">
      <div class="brand-mark" aria-hidden="true"></div>
      <h1 class="brand-name">
        <span class="line-primary">MERIDIAN</span>
        <span class="line-secondary">CHIROPRACTIC</span>
      </h1>
    </header>

    <section class="contact">
      <h2 class="contact-name">Firstname Lastname</h2>
      <p class="contact-title">Title</p>
      <p class="contact-details">
        Email: name@email.com<br>
        Phone: 000.000.0000<br>
        www.website.com
      </p>
    </section>
  </div>
</body>
</html>
```